Quiet Harbor Hours Podcast Artwork

I need a cover for my podcast Quiet Harbor Hours that is clean, modern, and minimalist, but not too feminine

Target Market(s)

People struggling with fertility particularly women who are between the ages of 35-45 though there is a small set of listeners who are men

Requirements
Must have
• Embryo in the Zero
Should not have
• No script text

```html
<!DOCTYPE html>
<html lang="en">
<head>
<meta charset="UTF-8">
<title>Quiet Harbor Hours – Podcast Cover</title>
<link href="https://fonts.googleapis.com/css2?family=Playfair+Display:wght@400&family=Lato:wght@300&display=swap" rel="stylesheet">
<style>
  :root {
    --paper: #f8f8f8;
    --sand: #b4a584;
    --sand-light: #c8b792;
    --sage: #9eab8d;
    --sage-shade: #919f7f;
    --blush: #f6e0d6;
    --blush-edge: #ffffff;
    --ink-light: #f8f8f8;
  }
  html, body {
    margin: 0;
    padding: 0;
    width: 1200px;
    height: 1200px;
    overflow: hidden;
    background: var(--paper);
  }
  .cover {
    position: relative;
    width: 1200px;
    height: 1200px;
    background: var(--paper);
  }
  .cover__art {
    position: absolute;
    inset: 0;
    width: 1200px;
    height: 1200px;
    display: block;
  }
  .tone-sand { fill: var(--sand); }
  .tone-sand-light { fill: var(--sand-light); }
  .tone-sage { fill: var(--sage); }
  .tone-sage-shade { fill: var(--sage-shade); }
  .figure-area {
    fill: var(--blush);
    stroke: var(--blush-edge);
    stroke-width: 5;
  }
  .cover__title {
    position: absolute;
    left: 724px;
    top: 742px;
    width: 340px;
    color: var(--ink-light);
    margin: 0;
  }
  .cover__title-main {
    display: block;
    font-family: "Playfair Display", Georgia, serif;
    font-weight: 400;
    font-size: 124px;
    line-height: 1;
    letter-spacing: -1px;
  }
  .cover__title-sub {
    display: block;
    margin-top: 26px;
    font-family: "Lato", Arial, sans-serif;
    font-weight: 300;
    font-size: 50px;
    line-height: 1;
    letter-spacing: 0.5px;
  }
</style>
</head>
<body>
  <main class="cover">
    <svg class="cover__art" viewBox="0 0 1500 1500" xmlns="http://www.w3.org/2000/svg">
      <!-- background panels -->
      <rect class="tone-sand" x="33" y="33" width="700" height="1434"/>
      <polygon class="tone-sand-light" points="33,1467 560,1080 733,1080 733,1467"/>
      <rect class="tone-sage" x="733" y="33" width="734" height="1434"/>
      <polygon class="tone-sage-shade" points="733,120 780,180 1467,1000 1467,1467 733,1467"/>
      <!-- central figure artwork area -->
      <rect class="figure-area" x="520" y="22" width="320" height="1466" rx="150"
            role="img" aria-label="Line illustration of two facing profiles forming a single soft blush silhouette"/>
    </svg>
    <h1 class="cover__title">
      <span class="cover__title-main">Quiet</span>
      <span class="cover__title-sub">Harbor Hours</span>
    </h1>
  </main>
</body>
</html>
```